Business Card design for Founder and CEO of new shoe company

I am looking for a business card design for my new shoe company called Strapwell.

I am launching the company this April. Strapwell shoes offers slip-on athletic and casual style shoes for men and women. The unique selling point of the brand is that all of our shoe exist without shoelaces. I have included a link to the website to offer additional information about the company, see product images, and gain inspiration for the design. You can use the store owner password "Strapwell" to access the website.

www.Strapwell.example

Thanks,
Dan Hollis

Target Market(s)

Active Men and Women ages 16-45

Industry/Entity Type

Business

Contact Information for Business Card

Dan Hollis
Founder and CEO
www.Strapwell.example
danhollis@Strapwell.example
888-555-0187 / 888-5STRAPW
Strapwell, LLC
2284 N Tamsin Ave
Chicago, IL 60699

Requirements
Must have
• Be able to quickly and easily tell that Strapwell is a shoe company from the business card

```html
<!DOCTYPE html>
<html lang="en">
<head>
<meta charset="utf-8">
<title>Strapwell Business Card</title>
<link href="https://fonts.googleapis.com/css2?family=Open+Sans:wght@300;400;700&display=swap" rel="stylesheet">
<style>
  :root {
    --page: #e9e9eb;
    --card-black: #000000;
    --ink-white: #ffffff;
    --rule-grey: #9a9a9a;
    --photo-light: #f4f4f4;
    --photo-mid: #dcdcdc;
    --band-grey: #a9a9ab;
  }
  * { box-sizing: border-box; margin: 0; padding: 0; }
  html, body {
    width: 1200px; height: 900px; overflow: hidden;
    background: var(--page);
    font-family: "Open Sans", Arial, sans-serif;
  }
  .canvas {
    position: relative; width: 1200px; height: 900px;
  }
  .card {
    position: absolute; left: 260px;
    width: 680px; height: 389px;
    border-radius: 22px; overflow: hidden;
    background: var(--card-black);
    box-shadow: 0 8px 24px rgba(0,0,0,.25);
  }
  .card--front { top: 50px; }
  .card--back { top: 461px; }

  /* front */
  .product-photo {
    position: absolute; left: 0; top: 0; width: 100%; height: 212px;
    background: linear-gradient(180deg, var(--photo-light) 0%, var(--photo-mid) 100%);
  }
  .photo-band {
    position: absolute; left: 0; top: 212px; width: 100%; height: 10px;
    background: var(--band-grey);
  }
  .brand-name {
    position: absolute;
    color: var(--ink-white);
    font-weight: 300;
    letter-spacing: 2px;
    line-height: 1;
  }
  .card--front .brand-name { left: 210px; top: 262px; font-size: 64px; }

  /* back */
  .card--back .brand-name { left: 200px; top: 60px; font-size: 64px; }
  .address {
    position: absolute; right: 28px; top: 176px;
    color: var(--ink-white); font-size: 15px; text-align: right; line-height: 1.35;
  }
  .rule {
    position: absolute; height: 1px; background: var(--rule-grey);
  }
  .rule--address { right: 0; top: 226px; width: 400px; }
  .rule--name { left: 245px; top: 268px; width: 435px; }
  .edge-dot {
    position: absolute; left: -14px; top: 260px;
    width: 28px; height: 28px; border-radius: 50%;
    background: var(--ink-white);
  }
  .person {
    position: absolute; left: 30px; top: 248px; color: var(--ink-white);
  }
  .person-name { font-weight: 700; font-size: 24px; letter-spacing: 1px; line-height: 1; }
  .person-title { font-size: 15px; margin-top: 4px; }
  .contact-list {
    position: absolute; left: 56px; top: 304px; list-style: none;
    color: var(--ink-white); font-size: 15px; line-height: 22px;
  }
  .contact-list li { display: flex; align-items: center; gap: 8px; }
  .contact-list svg { width: 12px; height: 12px; flex: none; }
</style>
</head>
<body>
<main class="canvas">
  <section class="card card--front">
    <div class="product-photo" role="img" aria-label="Row of colourful laceless athletic sneakers in pink, blue, teal and navy on a white backdrop"></div>
    <div class="photo-band"></div>
    <div class="brand-name">Strapwell</div>
  </section>

  <section class="card card--back">
    <div class="brand-name">Strapwell</div>
    <p class="address">Strapwell, LLC 2284<br>N Tamsin Ave Chicago, IL 60699</p>
    <div class="rule rule--address"></div>
    <div class="edge-dot"></div>
    <div class="person">
      <p class="person-name">DAN HOLLIS</p>
      <p class="person-title">Founder and CEO</p>
    </div>
    <div class="rule rule--name"></div>
    <ul class="contact-list">
      <li>
        <svg viewBox="0 0 12 12" aria-hidden="true"><path d="M2.5 1 L4.5 1 L5.2 3.6 L4 4.6 Q5 7 7.4 8 L8.4 6.8 L11 7.5 L11 9.5 Q11 11 9.5 11 Q1 10 1 2.5 Q1 1 2.5 1Z" fill="#fff"/></svg>
        888-555-0187 / 888-5STRAPW
      </li>
      <li>
        <svg viewBox="0 0 12 12" aria-hidden="true"><rect x="1" y="2.5" width="10" height="7" fill="none" stroke="#fff" stroke-width="1.2"/><path d="M1 2.5 L6 6.5 L11 2.5" fill="none" stroke="#fff" stroke-width="1.2"/></svg>
        danhollis@Strapwell.example
      </li>
      <li>
        <svg viewBox="0 0 12 12" aria-hidden="true"><circle cx="6" cy="6" r="5" fill="none" stroke="#fff" stroke-width="1.1"/><ellipse cx="6" cy="6" rx="2.2" ry="5" fill="none" stroke="#fff" stroke-width="1"/><path d="M1 6 H11" stroke="#fff" stroke-width="1"/></svg>
        www.Strapwell.example
      </li>
    </ul>
  </section>
</main>
</body>
</html>
```